Design a Website for an IT Support Company

We are an IT support company that provides commercial IT support and services to small and medium sized businesses. We are in need of a website to be developed for our business.
We would like to work with someone who is either familiar with the IT field, or has developed a website for an IT support company in the past.
Some examples of designs/layouts that we like:
https://www.velmorask.example/
http://www.quibenstack.example/
http://572zo.example/
http://www.guspelnetworks.example/
http://www.ourba.example/
I have attached a word document that gives a menu system/page layout format that we would like for our website as well as branch office phone numbers. Our logo is also attached that you can use for your design purposes. We currently do not have copy produced for all of the pages outlined in the word document, but would get this done during the project with the selected designer.
We would like the website to be SEO friendly & fully responsive. We would prefer a Wordpress format, however, we are open to HTML formats as well.

```html
<!DOCTYPE html>
<html lang="en">
<head>
<meta charset="utf-8">
<title>Corvane IT – IT Support</title>
<link href="https://fonts.googleapis.com/css2?family=Raleway:wght@400;500;600;700&family=Open+Sans:wght@400;600&display=swap" rel="stylesheet">
<style>
:root{
  --blue:#0a4ea8;
  --blue-bright:#1f6fd1;
  --blue-bar:#2a73d0;
  --navy:#0b2a5a;
  --ink:#1c1c1c;
  --text:#555;
  --muted:#888;
  --grey-bg:#efefef;
  --field:#d6d6d8;
  --dark:#2f2f2f;
  --darker:#1d1d1d;
  --white:#fff;
}
*{box-sizing:border-box;margin:0;padding:0}
html,body{width:1200px;height:3429px;overflow:hidden}
body{position:relative;font-family:"Open Sans",Arial,sans-serif;color:var(--text);background:var(--white)}
section,header,footer{position:absolute;left:0;width:1200px}
.abs{position:absolute}

/* header */
.site-header{top:0;height:88px;background:var(--white)}
.brand{left:92px;top:22px;display:flex;align-items:center;gap:12px;font-family:"Raleway",sans-serif;font-weight:700;font-size:30px;color:var(--ink)}
.brand-dot{width:34px;height:34px;border-radius:50%;background:var(--blue)}
.main-nav{right:80px;top:0;display:flex;gap:34px;height:88px;align-items:center}
.main-nav a{font-family:"Raleway",sans-serif;font-size:13px;font-weight:600;color:var(--ink);text-decoration:none;text-transform:uppercase;position:relative;height:88px;line-height:88px}
.main-nav a.active::after{content:"";position:absolute;left:0;right:0;bottom:0;height:4px;background:var(--ink)}

/* hero */
.hero{top:88px;height:490px;background:linear-gradient(100deg,#0f4d8f 0%,#1f6fc4 40%,#5b9ad8 62%,#0d2c56 100%)}
.hero-photo{position:absolute;inset:0;background:radial-gradient(circle at 62% 40%,rgba(190,225,255,.55),rgba(20,60,120,0) 45%)}
.hero h1{left:87px;top:138px;font-family:"Raleway",sans-serif;font-weight:700;font-size:41px;line-height:46px;color:var(--white)}
.hero p{left:87px;top:237px;width:420px;font-size:13px;line-height:20px;color:#e4eefb}
.btn-dark{left:85px;top:314px;width:200px;height:38px;border-radius:8px;background:#2b2b2b;color:var(--white);font-size:14px;line-height:38px;text-align:center}

/* welcome */
.welcome{top:578px;height:432px;text-align:center}
.eyebrow{top:54px;width:100%;font-family:"Raleway",sans-serif;font-size:14px;color:var(--muted)}
.section-title{width:100%;font-family:"Raleway",sans-serif;font-weight:600;font-size:28px;color:var(--ink);letter-spacing:.5px}
.welcome .section-title{top:80px}
.welcome .copy{left:130px;width:940px;font-size:13px;line-height:22px;color:var(--text)}
.btn-blue{background:var(--blue);color:var(--white);font-weight:600;font-size:13px;text-align:center;border-radius:4px}
.welcome .btn-blue{left:530px;top:337px;width:140px;height:40px;line-height:40px}

/* how it works */
.how{top:1010px;height:630px;background:var(--grey-bg)}
.how .section-title{top:50px;text-align:center}
.title-rule{left:560px;width:80px;height:2px;background:var(--blue)}
.service-card{top:255px;width:310px;height:315px;background:var(--white);border:1px solid #ddd;border-radius:14px;text-align:center}
.service-card h3{margin-top:106px;font-family:"Raleway",sans-serif;font-weight:500;font-size:26px;color:var(--ink)}
.service-card p{margin:18px auto 0;width:250px;font-size:13px;line-height:26px;color:#777}
.service-icon{top:165px;width:150px;height:150px;border-radius:50%;background:var(--white);border:5px solid var(--blue);display:flex;align-items:center;justify-content:center}

/* why */
.why{top:1640px;height:675px}
.why .section-title{top:40px;text-align:center}
.why .lead{top:140px;width:100%;text-align:center;font-size:14px;color:#666}
.feature-art{border-radius:6px}
.feature h3{font-family:"Raleway",sans-serif;font-weight:600;font-size:19px;color:#333;letter-spacing:.5px}
.feature p{font-family:"Raleway",sans-serif;font-size:15px;line-height:28px;color:#666}

/* faq + contact */
.help{top:2315px;height:470px;background:var(--grey-bg)}
.help h2{font-family:"Raleway",sans-serif;font-weight:600;font-size:20px;color:var(--ink)}
.faq-bar{left:100px;width:485px;height:38px;background:var(--blue-bar);color:var(--white);font-family:"Raleway",sans-serif;font-size:14px;font-weight:500;line-height:38px;padding-left:16px;border-radius:2px}
.faq-bar span{display:inline-block;width:20px;font-weight:700}
.faq-answer{left:110px;top:145px;width:470px;font-family:"Raleway",sans-serif;font-size:13px;line-height:21px;color:#555}
.field{background:var(--field);font-size:11px;color:#888;padding:0 14px;display:flex;align-items:center}
.btn-submit{left:972px;top:387px;width:111px;height:40px;line-height:40px;background:#0846c9;color:var(--white);font-size:11px;font-weight:600;text-align:center;border-radius:2px}

/* reviews */
.reviews{top:2785px;height:320px;background:var(--dark)}
.reviews-title{left:87px;top:125px;font-family:"Raleway",sans-serif;font-size:26px;line-height:30px;color:var(--white)}
.reviews-title strong{display:block;color:var(--blue-bright);font-weight:700;letter-spacing:1px}
.reviews .divider{left:307px;top:26px;width:2px;height:270px;background:#777}
.quote-badge{left:277px;top:130px;width:62px;height:62px;border-radius:50%;background:var(--white);color:var(--ink);font-family:Georgia,serif;font-size:44px;font-weight:700;text-align:center;line-height:72px}
.avatar{left:692px;top:38px;width:76px;height:82px}
.quote{left:390px;top:135px;width:680px;text-align:center;font-family:"Open Sans",sans-serif;font-style:italic;font-size:16px;line-height:30px;color:#ddd}
.arrow{top:146px;color:#ccc;font-size:22px}
.cite{left:390px;top:235px;width:680px;text-align:center;font-size:11px;font-style:italic;color:#ddd}

/* footer */
.site-footer{top:3105px;height:280px}
.footer-left{left:0;top:0;width:502px;height:280px;background:var(--blue)}
.footer-left h4{position:absolute;left:87px;top:48px;font-family:"Raleway",sans-serif;font-weight:700;font-size:16px;color:var(--white)}
.footer-left .rule{position:absolute;left:87px;top:80px;width:195px;height:2px;background:var(--white)}
.quick-links{position:absolute;top:112px;list-style:none}
.quick-links li{font-family:"Raleway",sans-serif;font-size:14px;color:var(--white);height:32px;padding-left:16px;position:relative}
.quick-links li::before{content:"";position:absolute;left:0;top:7px;width:8px;height:8px;border-radius:50%;background:var(--white)}
.footer-right h4{font-family:"Raleway",sans-serif;font-weight:700;font-size:17px;color:var(--ink)}
.footer-right p{font-size:11px;line-height:16px;color:#777}
.signup-field{left:590px;top:168px;width:340px;height:46px;border:1px solid #ccc;background:#f0f0f0;font-size:11px;color:#999;padding-left:14px;line-height:44px}
.btn-go{left:948px;top:168px;width:112px;height:46px;line-height:46px;background:var(--blue);color:var(--white);font-weight:700;font-size:14px;text-align:center}
.copyright{top:3385px;height:44px;background:var(--darker);color:#ddd;font-size:12px;text-align:center;line-height:44px}
</style>
</head>
<body>

<header class="site-header">
  <div class="brand abs"><span class="brand-dot"></span>Corvane IT</div>
  <nav class="main-nav abs">
    <a class="active">Home</a><a>Services</a><a>Why Corvane IT</a><a>Contact Us</a>
  </nav>
</header>

<section class="hero">
  <div class="hero-photo" role="img" aria-label="Businessman touching a glowing screen of technology icons"></div>
  <h1 class="abs">Get more from<br>your technology</h1>
  <p class="abs">With over 25 years experience and real focus on customer satisfaction, you can rely on us for your next renovation.</p>
  <div class="btn-dark abs">Experience worry-free IT</div>
</section>

<section class="welcome">
  <div class="eyebrow abs">All Types of Services - Build your feature!</div>
  <h2 class="section-title abs">WELCOME TO CORVANE IT</h2>
  <p class="copy abs" style="top:150px">With over 25 years experience and real focus on customer satisfaction, you can rely on us for your next renovation, driveway sett or home repair. We provide a professional service for private and commercial customers.Lorem Ipsum is simply dummy text of the printing and typesetting industry. Lorem Ipsum has been the industry's standard dummy text ever since the 1500s, when an unknown printer took a galley of type and scrambled it to make a type specimen book. It has survived not only five centuries, but also the leap into electronic typesetting, remaining essentially unchanged.</p>
  <p class="copy abs" style="top:258px">It was popularised in the 1960s with the release of Brellix sheets containing Lorem Ipsum passages, and more recently with desktop publishing software like Quadrel PageSetter including versions of Lorem Ipsum.</p>
  <div class="btn-blue abs">READ MORE</div>
</section>

<section class="how">
  <h2 class="section-title abs">HOW IT WORKS ?</h2>
  <div class="title-rule abs" style="top:108px"></div>

  <div class="service-card abs" style="left:103px"><h3>DATA</h3><p>We put a lot of effort in design, as it's the most important ingredient of successful website.Sed ut perspiciatis unde omnis iste natus error sit.</p></div>
  <div class="service-card abs" style="left:450px"><h3>CLOUD</h3><p>We put a lot of effort in design, as it's the most important ingredient of successful website.Sed ut perspiciatis unde omnis iste natus error sit.</p></div>
  <div class="service-card abs" style="left:798px"><h3>VOICE</h3><p>We put a lot of effort in design, as it's the most important ingredient of successful website.Sed ut perspiciatis unde omnis iste natus error sit.</p></div>

  <div class="service-icon abs" style="left:183px">
    <svg width="70" height="70" viewBox="0 0 70 70" fill="none" stroke="#222" stroke-width="3"><path d="M8 34 35 10 62 34"/><path d="M16 28v32h38V28"/><path d="M29 60V42h12v18"/><path d="M48 16v10"/></svg>
  </div>
  <div class="service-icon abs" style="left:530px">
    <svg width="76" height="70" viewBox="0 0 76 70" fill="#222"><circle cx="20" cy="22" r="10"/><circle cx="56" cy="22" r="10"/><path d="M4 60c0-14 7-24 16-24s12 6 12 6v18z"/><path d="M72 60c0-14-7-24-16-24s-12 6-12 6v18z"/><circle cx="38" cy="20" r="13"/><path d="M18 64c0-18 9-30 20-30s20 12 20 30z"/></svg>
  </div>
  <div class="service-icon abs" style="left:878px">
    <svg width="68" height="68" viewBox="0 0 68 68" fill="none" stroke="#222" stroke-width="3"><circle cx="34" cy="34" r="26"/><ellipse cx="34" cy="34" rx="11" ry="26"/><path d="M8 34h52M13 20h42M13 48h42"/></svg>
  </div>
</section>

<section class="why">
  <h2 class="section-title abs">WHY CHOOSE US?</h2>
  <p class="lead abs">Choose our very cheap and best quality hosting services package and run your business like a boss.</p>

  <div class="feature-art abs" style="left:120px;top:225px;width:225px;height:190px;background:linear-gradient(160deg,#eef2f6,#d9e4ef)" role="img" aria-label="Smartphone with floating colourful app icons"></div>
  <div class="feature abs" style="left:438px;top:223px;width:600px">
    <h3>GREAT USER EXPERIENCE</h3>
    <p style="margin-top:8px">Signs beast together said earth our fowl signs. Fowl it made years gather. Above may fruitful him. Them day brought place and saw Third. Every from together days life also dream. Signs beast together said earth our fowl signs. Fowl made years gather. Above may him. Them day brought place and saw Third. Every from together days life also dream has come true finally.</p>
  </div>

  <div class="feature abs" style="left:120px;top:415px;width:580px">
    <h3 style="margin-left:318px">GLOBAL COMMUNICATION</h3>
    <p style="margin-top:8px;text-align:right">Signs beast together said earth our fowl signs. Fowl it made years gather. Above may fruitful him. Them day brought place and saw Third. Every from together days life also dream. Signs beast together said earth our fowl signs. Fowl made years gather. Above may him. Them day brought place and saw Third. Every from together days life also dream has come true finally.</p>
  </div>
  <div class="feature-art abs" style="left:755px;top:415px;width:285px;height:190px;background:linear-gradient(160deg,#f2faf5,#dff0e6)" role="img" aria-label="Hand holding a phone surrounded by app icons"></div>
</section>

<section class="help">
  <h2 class="abs" style="left:100px;top:50px">Faq's</h2>
  <div class="faq-bar abs" style="top:100px"><span>−</span>Dolor sit amet adipiscing</div>
  <p class="faq-answer abs">Open place fly light dry. Had may green ca Winged make dry wherein set ownland tree two of thing wont female of from two the Youre were our whose. Herb male also Face multiply n'owl winged face Fruitful moveth land. Herb male also Face multiply fowl winged.</p>
  <div class="faq-bar abs" style="top:250px"><span>+</span>Anim pariatur cliche reprit</div>
  <div class="faq-bar abs" style="top:294px"><span>+</span>Laborum eiusmod tempor sunt</div>
  <div class="faq-bar abs" style="top:338px"><span>+</span>Accusamus terry richard squid</div>
  <div class="faq-bar abs" style="top:382px"><span>+</span>Youre of from two the Youre were</div>

  <h2 class="abs" style="left:635px;top:50px">Get In Touch With Us Today</h2>
  <p class="abs" style="left:635px;top:78px;font-family:Raleway,sans-serif;font-size:15px;color:#555">You've got questions, and we have answers.</p>
  <div class="field abs" style="left:635px;top:124px;width:450px;height:42px;justify-content:space-between;color:#444">Discuss with Financial Experts<span>▾</span></div>
  <div class="field abs" style="left:635px;top:196px;width:210px;height:42px">Name</div>
  <div class="field abs" style="left:872px;top:196px;width:213px;height:42px">Email</div>
  <div class="field abs" style="left:635px;top:265px;width:450px;height:100px;align-items:flex-start;padding-top:10px">Message</div>
  <div class="btn-submit abs">SUBMIT ➜</div>
</section>

<section class="reviews">
  <div class="reviews-title abs">Coustomers<strong>REVIEWS</strong></div>
  <div class="divider abs"></div>
  <div class="quote-badge abs">“</div>
  <svg class="avatar abs" viewBox="0 0 76 82" role="img" aria-label="Customer portrait"><path d="M38 2 72 21v40L38 80 4 61V21z" fill="#ddd" stroke="#fff" stroke-width="3"/><path d="M38 10 65 25v32L38 72 11 57V25z" fill="#b48a6e"/></svg>
  <div class="arrow abs" style="left:360px">←</div>
  <p class="quote abs">“The benefits of psychological capital appear to be as central to the success of entrepreneurs as more traditional forms of capital.”</p>
  <div class="arrow abs" style="left:1095px">→</div>
  <p class="cite abs">(“The Role of Affect in the Entrepreneurial Process,” R.L. Danvers, The Journal of Venture Studies, Vol. 33 (2).</p>
</section>

<footer class="site-footer">
  <div class="footer-left abs">
    <h4>Quick Links•</h4>
    <div class="rule"></div>
    <ul class="quick-links" style="left:87px"><li>Home</li><li>About Us</li><li>Contact Us</li><li>Our Firm</li></ul>
    <ul class="quick-links" style="left:213px"><li>Our Story</li><li>Our Services</li><li>Problems and Solutions</li><li>Group &amp; Relationship Models</li></ul>
  </div>
  <svg class="abs" style="left:432px;top:92px" width="110" height="110" viewBox="0 0 110 110">
    <path d="M55 5 105 55 55 105 5 55z" fill="#fff"/>
    <path d="M55 5 105 55 55 105z" fill="#111"/>
    <g fill="none" stroke="#111" stroke-width="4" stroke-linecap="round"><path d="M26 60l8-8M22 58a5 5 0 0 1 0-7l6-6a5 5 0 0 1 7 0M38 50a5 5 0 0 1 0 7l-6 6a5 5 0 0 1-7 0"/></g>
    <g fill="none" stroke="#fff" stroke-width="4" stroke-linecap="round"><path d="M66 46h16l-5-5M84 64H68l5 5"/></g>
  </svg>
  <div class="footer-right">
    <h4 class="abs" style="left:578px;top:28px">The Corvane IT</h4>
    <p class="abs" style="left:578px;top:54px;width:500px">No matter how successful you are as an entrepreneur, there are always higher levels you want to achieve in both your business and personal life – two areas that are inseparable and continuously impacting each other.&nbsp; Our services are transformative.</p>
    <h4 class="abs" style="left:590px;top:130px;font-weight:600">Sign up for updates</h4>
    <div class="signup-field abs">Enter Your Email Address</div>
    <div class="btn-go abs">GO</div>
  </div>
</footer>

<footer class="copyright">Copyright 2017 - All Rights Reserved</footer>

</body>
</html>
```